My business is Property developing Stationary

I want business card and stationery. Please have the formate so I can edit details on card and stationary.

Please see my logo and on the back of the card I want it same red as my logo and I will provide copy that I want on the back of the card.

Also need an email signature

On the business card and email signature add below copy:
Project Management- Acquisitions- Syndicates- Joint Ventures

Target Market(s)

Property investors

Industry/Entity Type

Business

Requirements
Must have
• Reflect my Logo

```html
<!DOCTYPE html>
<html lang="en">
<head>
<meta charset="UTF-8">
<title>Calder Property Developments – Letterhead</title>
<link rel="stylesheet" href="https://fonts.googleapis.com/css2?family=Montserrat:wght@400;700&display=swap">
<style>
  :root {
    --brand-red: #e8453a;
    --ink-grey: #6f6f6f;
    --ink-dark: #222222;
    --paper: #ffffff;
  }
  html, body {
    margin: 0;
    padding: 0;
    overflow: hidden;
    background: var(--paper);
  }
  .letterhead {
    position: relative;
    width: 848px;
    height: 1200px;
    background: var(--paper);
    overflow: hidden;
    font-family: "Montserrat", Arial, sans-serif;
  }
  .edge-bar {
    position: absolute;
    left: 0;
    top: 26px;
    width: 10px;
    height: 114px;
    background: var(--brand-red);
  }
  .brand-name {
    position: absolute;
    left: 48px;
    top: 72px;
    margin: 0;
    color: var(--brand-red);
    font-weight: 700;
    line-height: 1;
  }
  .brand-name .brand-main {
    display: block;
    font-size: 44px;
    letter-spacing: 2px;
  }
  .brand-name .brand-sub {
    display: block;
    margin-top: 6px;
    font-size: 16.5px;
    letter-spacing: 0.2px;
  }
  .contact-block {
    position: absolute;
    right: 42px;
    top: 92px;
    text-align: right;
    color: var(--ink-grey);
    font-weight: 400;
  }
  .contact-address,
  .contact-numbers {
    font-size: 11.5px;
    letter-spacing: 0.3px;
    line-height: 1;
  }
  .contact-numbers {
    margin-top: 9px;
    padding-bottom: 5px;
    border-bottom: 1px solid #9a9a9a;
  }
  .contact-web {
    margin-top: 6px;
    font-size: 9.5px;
    letter-spacing: 0.2px;
  }
  .contact-web .gap { display: inline-block; width: 12px; }
  .dot {
    display: inline-block;
    width: 4px;
    height: 4px;
    margin: 0 5px 2px;
    vertical-align: middle;
    background: var(--ink-dark);
  }
  .dot--red { background: var(--brand-red); }
  .footer-band {
    position: absolute;
    left: 0;
    bottom: 0;
    width: 848px;
    height: 40px;
    background: var(--brand-red);
  }
  .footer-web {
    position: absolute;
    right: 42px;
    top: 11px;
    color: #ffffff;
    font-size: 15.5px;
    font-weight: 700;
    letter-spacing: 0.3px;
    line-height: 1;
  }
</style>
</head>
<body>
  <main class="letterhead">
    <div class="edge-bar"></div>

    <h1 class="brand-name">
      <span class="brand-main">CALDER</span>
      <span class="brand-sub">Property Developments</span>
    </h1>

    <address class="contact-block" style="font-style: normal;">
      <div class="contact-address">418 Maple Avenue Portland, OR 97205-1142 USA</div>
      <div class="contact-numbers">Phone 021 555 0146<span class="dot"></span>Fax 021 555 0188<span class="dot dot--red"></span>Cell 0955 501 234</div>
      <div class="contact-web">Email: ana.reyes@calderproperty.com<span class="gap"></span>Web: calderproperty.com</div>
    </address>

    <footer class="footer-band">
      <span class="footer-web">www.Calderproperty.com</span>
    </footer>
  </main>
</body>
</html>
```